Business Card and Letterhead for Vantage Psychology

We need a business card design and letterhead to use for our Psychology firm that specializes in psychoeducational assessments and individual therapy. Our motto is Purpose-Driven Assessments, Meaning-Centered Therapy.Our contact information is as follows:
Vantage Psychology
The Marwick Block - 6127-48St.
Box 2716 Brackwell, WR
T2K 3M8
t 403.555.0148 (VANT)
f 403.555.0172
www.vantagepsychology-example.ca
The business card will be used for two different psychologists so I can supply names nearer to completion. We prefer clean, uncluttered looks.

Target Market(s)

Clients, Educators

Font styles to use
Sans Serif

Colors

Designer to choose colors to be used in the design.

Requirements
Must have
• All relevant contact info, logo, some "white" space.
Nice to have
• It would be nice to see letterhead options that have the logo on the top of the page but also options that have it on the side. I think top of the page is probably our preference.
Should not have
• Too much clutter!

```html
<!DOCTYPE html>
<html lang="en">
<head>
<meta charset="utf-8">
<title>Vantage Psychology — Letterhead</title>
<link href="https://fonts.googleapis.com/css2?family=Open+Sans:wght@400;600&family=Roboto:wght@500&display=swap" rel="stylesheet">
<style>
  :root {
    --brand-blue: #55bedb;
    --brand-orange: #fdab48;
    --icon-orange: #f8a650;
    --ink: #111111;
    --paper: #ffffff;
  }
  html, body { margin: 0; padding: 0; overflow: hidden; background: var(--paper); }
  .letterhead {
    position: relative;
    width: 848px;
    height: 1200px;
    overflow: hidden;
    background: var(--paper);
    font-family: "Open Sans", Arial, sans-serif;
    color: var(--ink);
  }
  .brand {
    position: absolute;
    left: 45px;
    top: 47px;
    width: 240px;
    display: flex;
    flex-direction: column;
    align-items: center;
  }
  .brand-mark {
    width: 72px;
    height: 72px;
    border-radius: 50%;
    background: var(--brand-blue);
    margin-top: 21px;
  }
  .brand-name {
    margin-top: 2px;
    font-size: 19px;
    font-weight: 600;
    letter-spacing: 0.5px;
    color: var(--brand-blue);
    white-space: nowrap;
  }
  .letter-body {
    position: absolute;
    left: 67px;
    top: 352px;
    width: 714px;
    font-size: 14.6px;
    line-height: 20.4px;
    letter-spacing: -0.2px;
    text-align: justify;
  }
  .letter-body p { margin: 0 0 20.4px; }
  .signature {
    position: absolute;
    left: 595px;
    top: 836px;
    width: 201px;
    height: 110px;
    background: linear-gradient(135deg, #f4f4f4, #e9e9e9);
    border-radius: 4px;
  }
  .contact {
    position: absolute;
    font-family: "Roboto", Arial, sans-serif;
    font-weight: 500;
    font-size: 9px;
    letter-spacing: 1px;
    line-height: 11px;
    white-space: nowrap;
  }
  .contact-icon { position: absolute; fill: var(--icon-orange); }
  .phone-icon { left: 80px; top: 1087px; width: 33px; height: 36px; }
  .web-icon { left: 328px; top: 1089px; width: 21px; height: 33px; }
  .pin-icon { left: 572px; top: 1088px; width: 26px; height: 35px; }
  .phone-1 { left: 127px; top: 1088px; }
  .phone-2 { left: 127px; top: 1111px; }
  .web { left: 357px; top: 1099px; }
  .address { left: 615px; top: 1094px; }
  .address span { display: block; }
  .address .indent { padding-left: 2px; }
  .footer-band { position: absolute; top: 1155px; height: 45px; }
  .footer-band.blue { left: 0; width: 516px; background: var(--brand-blue); }
  .footer-band.orange { left: 516px; width: 332px; background: var(--brand-orange); }
</style>
</head>
<body>
<main class="letterhead">
  <header class="brand">
    <div class="brand-mark" aria-hidden="true"></div>
    <div class="brand-name">VANTAGE PSYCHOLOGY</div>
  </header>

  <section class="letter-body">
    <p>Lorem ipsum dolor sit amet, consectetur adipiscing elit. Vestibulum tincidunt dapibus sapien a euismod. Nunc ac risus in justo pulvinar varius. Vivamus consectetur laoreet ante et molestie. Praesent metus est, varius ac vestibulum sit amet, ornare at sem. Cras rhoncus leo arcu, at molestie neque condimentum in. Suspendisse fermentum tortor in elit consectetur, commodo fermentum ex fermentum. Proin sed magna dapibus, scelerisque mauris ut, ornare velit. Nam non ante quis eros euismod efficitur sed non mi. Aliquam volutpat viverra nulla, et commodo justo viverra vitae.</p>
    <p>Nunc libero urna, maximus sed faucibus non, consectetur at quam. Proin quis semper magna, et ultricies velit. Suspendisse maximus, dolor et rhoncus mollis, lacus lorem semper enim, luctus maximus eros ante sed mi. Integer posuere fringilla luctus. Suspendisse ac ligula non nisi luctus convallis id ac sem. Nulla id rhoncus metus. Aliquam sit amet elementum orci. Fusce varius gravida velit non dictum. In quis eros leo. Cras bibendum auctor tortor id dignissim. Duis cursus, erat id mattis semper, dolor magna ullamcorper leo, ac elementum est nulla nec ligula.</p>
    <p>Quisque non ante a turpis lacinia ornare. Etiam leo tellus, pharetra at diam id, interdum egestas magna. Sed pharetra vel odio id commodo. Proin at est ut sapien congue sagittis non vitae libero. Sed ac euismod orci. Proin ac fermentum neque, hendrerit eleifend leo. Nam vitae nunc in neque tincidunt accumsan. Aliquam ac ante interdum, fringilla massa non, molestie est. Sed imperdiet sollicitudin condimentum. Mauris a risus imperdiet, lobortis sem sed, maximus purus. Aliquam erat volutpat.</p>
    <p>Donec vehicula viverra urna, nec dapibus diam commodo quis. Mauris eu nisi vitae nisi pretium vulputate. Ut pellentesque, est a pellentesque finibus, neque leo iaculis erat.</p>
  </section>

  <div class="signature" role="img" aria-label="Handwritten signature of the psychologist"></div>

  <footer>
    <svg class="contact-icon phone-icon" viewBox="0 0 24 26" aria-hidden="true">
      <path d="M5.5 1.5c1-.6 2.2-.3 2.8.7l2.2 3.8c.5.9.3 2-.5 2.6l-1.8 1.3c1 2.6 3 5 5.5 6.5l1.5-1.6c.7-.7 1.8-.8 2.6-.2l3.5 2.6c.9.7 1.1 1.9.5 2.8l-1.3 2c-.9 1.3-2.5 1.9-4 1.4C9.3 21.3 3.2 13.8 1.8 6.5c-.3-1.5.4-3 1.7-3.8z"/>
    </svg>
    <div class="contact phone-1">403.555.0148</div>
    <div class="contact phone-2">403.555.0172</div>

    <svg class="contact-icon web-icon" viewBox="0 0 14 22" aria-hidden="true">
      <path d="M0 0l14 12-6 .6 3.4 7.6-2.6 1.2-3.3-7.7L0 18z"/>
    </svg>
    <div class="contact web">www.vantagepsychology-example.ca</div>

    <svg class="contact-icon pin-icon" viewBox="0 0 24 32" aria-hidden="true">
      <path fill-rule="evenodd" d="M12 0C5.4 0 0 5.2 0 11.7 0 19 12 32 12 32s12-13 12-20.3C24 5.2 18.6 0 12 0zm0 6.5a5.2 5.2 0 1 1 0 10.4 5.2 5.2 0 0 1 0-10.4z"/>
    </svg>
    <div class="contact address">
      <span>The Marwick Block -6127-48St.</span>
      <span class="indent">Box 2716 Brackwell, WR</span>
    </div>

    <div class="footer-band blue"></div>
    <div class="footer-band orange"></div>
  </footer>
</main>
</body>
</html>
```